Trailridge Depot Website Redesign

I am seeking an eye-catching design for a UTV Wholesale parts website (trailridgedepot.com). I have made an initial attempt, but I lack the design expertise to achieve the desired look.
I would like the designers to consider the following website styles when creating the new design:
-RigHaven.com: This is the go to website for UTV parts and it has a great design, layout, speed, and product line.
-Wrenly.com: This site is not a UTV website; however, it is a design that I find to be very appealing and along the lines of what i am looking for.
For temporary use, please use products and product categories you see on https://www.quadbarnparts.com/
I have added my own logo to the contest, please use it in your design. I like the use of yellow within the color scheme to match my logo. However, i dont like the all black background that i ended up with on the current version of my site. So i would like something more like wrenly.com and righaven, where there are some darker colors used but not a full on black background.
Make sure you add in a vehicle year make and model selection tool somewhere at the top of the page
Make sure there is a megamenu with graphical category selections, like you see on the example websites.

```html
<!DOCTYPE html>
<html lang="en">
<head>
<meta charset="utf-8">
<title>Trailridge Depot – UTV Parts</title>
<link href="https://fonts.googleapis.com/css2?family=Oswald:wght@500;600;700&family=Roboto:wght@400;500;700&display=swap" rel="stylesheet">
<style>
:root{
  --yellow:#f1d517;
  --yellow-deep:#e3c90f;
  --ink:#222222;
  --muted:#777777;
  --panel:#ececec;
  --topbar:#e4e4e4;
  --footer:#2d2d2d;
  --white:#ffffff;
}
*{box-sizing:border-box;margin:0;padding:0}
html,body{width:1200px;height:3940px;overflow:hidden}
body{font-family:"Roboto",Arial,sans-serif;color:var(--ink);background:var(--white);position:relative}
ul{list-style:none}

.topbar{position:absolute;left:0;top:0;width:1200px;height:34px;background:var(--topbar);font-size:12px;color:#333;display:flex;align-items:center;padding-left:112px}
.topbar .sep{width:1px;height:16px;background:#bbb;margin:0 14px}
.topbar a{color:#111;font-weight:700;text-decoration:underline}

.header{position:absolute;left:0;top:34px;width:1200px;height:82px;background:var(--white)}
.brand{position:absolute;left:112px;top:24px;font-family:"Oswald",sans-serif;font-weight:700;font-size:29px;color:var(--yellow-deep);letter-spacing:.5px;line-height:34px}
.tagline{position:absolute;left:368px;top:34px;font-size:12px;color:#666;font-weight:500;letter-spacing:.3px}
.tagline b{color:#222}
.search{position:absolute;left:592px;top:24px;width:293px;height:34px;border:1px solid #ccc;border-radius:17px;font-size:12px;color:#999;padding:10px 16px}
.pill{position:absolute;top:25px;height:32px;border-radius:16px;font-size:12px;font-weight:700;display:flex;align-items:center;justify-content:center;gap:5px}
.pill.signin{left:902px;width:88px;background:#1d1d1d;color:#fff}
.pill.cart{left:1001px;width:88px;background:var(--yellow);color:#111}

.nav{position:absolute;left:0;top:116px;width:1200px;height:46px;background:var(--yellow)}
.nav li{position:absolute;top:15px;font-size:13px;font-weight:500;color:#222;letter-spacing:.3px;display:flex;align-items:center;gap:5px}
.caret{width:0;height:0;border-left:4px solid transparent;border-right:4px solid transparent;border-top:5px solid #222}
.caret.up{border-top:none;border-bottom:5px solid #222}

.hero{position:absolute;left:0;top:162px;width:1200px;height:471px;background:linear-gradient(90deg,#e6d21f 0%,#d8c850 22%,#c8b78a 45%,#a9b4c4 62%,#c79a6c 78%,#b07a50 100%)}
.hero-photo{position:absolute;left:560px;top:150px;width:560px;height:321px;background:radial-gradient(ellipse at 50% 55%,#4a3a34 0%,#7a5a48 40%,rgba(176,122,80,0) 75%)}
.hero-kicker{position:absolute;left:112px;top:124px;font-size:20px;color:#2a2a2a}
.hero-title{position:absolute;left:112px;top:170px;font-size:54px;line-height:60px;font-weight:700;color:#2b2b2b;letter-spacing:2px}

.mega{position:absolute;left:492px;top:159px;width:540px;height:181px;background:var(--white);box-shadow:0 4px 12px rgba(0,0,0,.15)}
.mega li{position:absolute;left:22px;display:flex;align-items:center;gap:9px;font-size:16px;font-weight:500;color:#111}
.mega .ico{width:15px;height:15px;border-radius:50%;border:3px solid var(--yellow)}
.mega-img{position:absolute;left:318px;top:12px;width:200px;height:153px;border-radius:50%;background:radial-gradient(circle at 40% 45%,#d9dde2 0%,#8c939c 35%,#2c2f33 60%,#ffffff 72%)}
.cursor{position:absolute}

.finder{position:absolute;left:112px;top:668px;width:976px;height:171px;background:var(--panel);border-radius:4px}
.finder h2{position:absolute;left:24px;top:33px;font-family:"Oswald",sans-serif;font-weight:600;font-size:26px;color:#222}
.select{position:absolute;top:89px;width:254px;height:41px;background:var(--white);border-radius:3px;font-size:14px;color:#666;padding:12px 18px}
.select::after{content:"";position:absolute;right:18px;top:15px;width:6px;height:6px;border-right:1.5px solid #666;border-bottom:1.5px solid #666;transform:rotate(45deg)}
.btn{display:flex;align-items:center;justify-content:center;background:var(--yellow);color:#111;font-weight:700;font-size:14px;border-radius:20px;letter-spacing:.3px}
.finder .btn{position:absolute;left:819px;top:89px;width:137px;height:39px}

.section-title{position:absolute;left:0;width:1200px;text-align:center;font-family:"Oswald",sans-serif;font-weight:600;font-size:40px;color:#222}

.card{position:absolute;width:313px;height:362px;background:var(--white);box-shadow:0 1px 6px rgba(0,0,0,.12)}
.card .heart{position:absolute;right:20px;top:28px}
.card .thumb{position:absolute;left:80px;top:55px;width:153px;height:175px}
.thumb.nut{background:radial-gradient(ellipse at 50% 45%,#f0f0f0 0%,#d8d8d8 50%,#ffffff 75%)}
.thumb.hook{top:55px;left:84px;width:146px;height:158px;background:linear-gradient(180deg,#8c8c8c 0%,#c8c8c8 50%,#7a7a7a 100%)}
.thumb.flares{background:linear-gradient(90deg,#ffffff 0%,#2b2b2b 12%,#ffffff 30%,#2b2b2b 50%,#ffffff 70%,#2b2b2b 88%,#ffffff 100%)}
.card .qv{position:absolute;left:88px;top:162px;width:138px;height:38px}
.card .name{position:absolute;left:25px;top:257px;width:280px;font-size:15px;line-height:26px;color:#333;white-space:nowrap}
.card .price{position:absolute;left:25px;top:315px;font-size:16px;font-weight:700;color:#222}
.arrow{position:absolute;width:36px;height:36px;border-radius:50%;display:flex;align-items:center;justify-content:center}
.arrow.dim{background:#666}
.arrow.dark{background:#111}

.featured{position:absolute;left:0;top:1435px;width:1200px;height:600px;background:linear-gradient(90deg,#000000 0%,#2a2505 25%,#8d7d10 55%,#d5c016 80%,#e6cf1a 100%)}
.featured .section-title{color:var(--white);top:58px}

.cat{position:absolute;width:313px;height:362px;background:var(--white);box-shadow:0 1px 6px rgba(0,0,0,.12)}
.cat .photo{position:absolute;left:0;top:0;width:313px;height:225px}
.cat .label{position:absolute;left:0;top:250px;width:313px;text-align:center;font-size:16px;font-weight:500;color:#222}
.cat .btn{position:absolute;left:88px;top:283px;width:138px;height:38px}
.learn{position:absolute;left:517px;top:3012px;width:165px;height:39px;background:#1f1f1f;color:#fff;border-radius:20px;display:flex;align-items:center;justify-content:center;font-size:14px;font-weight:700}
.texture{position:absolute;background:linear-gradient(160deg,rgba(200,200,200,0) 0%,rgba(190,190,190,.45) 60%,rgba(200,200,200,.15) 100%)}

.signup{position:absolute;left:0;top:3106px;width:1200px;height:471px;background:linear-gradient(180deg,#8a97a6 0%,#b8a58a 30%,#c98a4c 70%,#b06b34 100%)}
.signup-photo{position:absolute;left:640px;top:40px;width:420px;height:400px;background:radial-gradient(ellipse at 50% 50%,#2d3440 0%,#5a5550 40%,rgba(190,130,80,0) 72%)}
.signup h2{position:absolute;left:112px;top:150px;font-family:"Oswald",sans-serif;font-weight:600;font-size:40px;color:#fff}
.signup p{position:absolute;left:110px;top:203px;font-size:21px;color:#fff}
.signup .email{position:absolute;left:112px;top:251px;width:362px;height:57px;background:#fff;border-radius:3px;font-size:14px;color:#777;padding:20px 18px}
.signup .btn{position:absolute;left:112px;top:329px;width:138px;height:38px}

.footer{position:absolute;left:0;top:3577px;width:1200px;height:363px;background:var(--footer);color:#eee}
.footer .brand{left:118px;top:64px;font-size:28px;color:var(--yellow)}
.social{position:absolute;left:118px;top:130px;display:flex;gap:30px}
.social span{width:18px;height:18px;border-radius:50%;border:2px solid #eee}
.fcol{position:absolute;top:65px}
.fcol h4{font-family:"Oswald",sans-serif;font-weight:600;font-size:17px;color:#fff;margin-bottom:8px}
.fcol li{font-size:14px;line-height:30px;color:#eee}
.fcol.contact li{display:flex;gap:8px;align-items:flex-start;line-height:25px;margin-bottom:8px}
.copy{position:absolute;left:112px;top:270px;font-size:13px;line-height:25px;color:#eee}
</style>
</head>
<body>

<div class="topbar">Call us on: +1-800-555-0142<span class="sep"></span>Summer sale discount off 10%!&nbsp;<a>Shop Now</a></div>

<header class="header">
  <div class="brand">TRAILRIDGE DEPOT</div>
  <div class="tagline">ONE STOP SHOP FOR <b>UTV PARTS</b></div>
  <div class="search">Search here</div>
  <div class="pill signin">
    <svg width="10" height="11" viewBox="0 0 10 11"><circle cx="5" cy="3" r="2.6" fill="#fff"/><path d="M0 11c0-3.5 2.2-5 5-5s5 1.5 5 5z" fill="#fff"/></svg>Sign in</div>
  <div class="pill cart">
    <svg width="12" height="11" viewBox="0 0 12 11"><path d="M0 1h2l1.6 6h6.4l1.5-4.5H3" fill="none" stroke="#111" stroke-width="1.4"/><circle cx="4.5" cy="9.5" r="1.1" fill="#111"/><circle cx="9" cy="9.5" r="1.1" fill="#111"/></svg>Cart</div>
</header>

<nav class="nav">
  <ul>
    <li style="left:116px">HOME</li>
    <li style="left:191px">MAKES &amp; MODELS <span class="caret"></span></li>
    <li style="left:361px">PART TYPES <span class="caret"></span></li>
    <li style="left:492px">WHEELS &amp; TIRES <span class="caret up"></span></li>
    <li style="left:651px">BRANDS <span class="caret"></span></li>
    <li style="left:757px">SALES</li>
    <li style="left:835px">GALLERY</li>
    <li style="left:929px">MORE <span class="caret"></span></li>
    <li style="left:1018px">CONTACT</li>
  </ul>
</nav>

<section class="hero" role="img" aria-label="Off-road UTV parked on desert rocks under a clear sky">
  <div class="hero-photo"></div>
  <div class="hero-kicker">Emberlight Heat Guns</div>
  <h1 class="hero-title">FULL SATISFACTION<br>IN AFFORDABLE<br>PRICES</h1>
</section>

<div class="mega">
  <ul>
    <li style="top:34px"><span class="ico"></span>Wheels</li>
    <li style="top:76px"><span class="ico"></span>Tires</li>
    <li style="top:117px"><span class="ico"></span>Pre-Mounted Wheel &amp; Tire Kits</li>
  </ul>
  <div class="mega-img" role="img" aria-label="Pair of alloy wheels with tires"></div>
</div>
<svg class="cursor" style="left:606px;top:144px" width="22" height="30" viewBox="0 0 22 30"><path d="M7 2v14l-3-3c-1.5-1.5-3.5 0-2 2l6 8c1 1.5 2 3 5 3h3c3 0 5-2 5-5v-7c0-1.5-2-1.5-2 0v-2c0-1.5-2-1.5-2 0v-1c0-1.5-2-1.5-2 0V2c0-2-3-2-3 0z" fill="#fff" stroke="#111" stroke-width="1.3"/></svg>

<section class="finder">
  <h2>SHOP BY VEHICLE</h2>
  <div class="select" style="left:24px">Year</div>
  <div class="select" style="left:287px">Make</div>
  <div class="select" style="left:548px">Model</div>
  <div class="btn">SEARCH</div>
</section>

<div class="texture" style="left:552px;top:1355px;width:648px;height:80px"></div>

<h2 class="section-title" style="top:892px">NEW PRODUCTS</h2>

<div class="arrow dim" style="left:37px;top:1159px"><svg width="10" height="14" viewBox="0 0 10 14"><path d="M8 1L2 7l6 6" fill="none" stroke="#fff" stroke-width="2.4"/></svg></div>
<div class="arrow dim" style="left:1126px;top:1159px"><svg width="10" height="14" viewBox="0 0 10 14"><path d="M2 1l6 6-6 6" fill="none" stroke="#fff" stroke-width="2.4"/></svg></div>

<article class="card" style="left:112px;top:997px">
  <svg class="heart" width="26" height="22" viewBox="0 0 26 22"><path d="M13 21S1 13.5 1 6.5A5.5 5.5 0 0 1 13 4a5.5 5.5 0 0 1 12 2.5C25 13.5 13 21 13 21z" fill="#e8e8e8"/></svg>
  <div class="thumb nut" role="img" aria-label="Aluminium bed rail nut"></div>
  <div class="btn qv">QUICK VIEW</div>
  <svg class="cursor" style="left:222px;top:200px" width="20" height="27" viewBox="0 0 22 30"><path d="M7 2v14l-3-3c-1.5-1.5-3.5 0-2 2l6 8c1 1.5 2 3 5 3h3c3 0 5-2 5-5v-7c0-1.5-2-1.5-2 0v-2c0-1.5-2-1.5-2 0v-1c0-1.5-2-1.5-2 0V2c0-2-3-2-3 0z" fill="#fff" stroke="#111" stroke-width="1.3"/></svg>
  <p class="name">Kodo Offroad Summit TX 900<br>Bed Rail Nut</p>
  <p class="price">$5.90</p>
</article>
<article class="card" style="left:443px;top:997px">
  <svg class="heart" width="26" height="22" viewBox="0 0 26 22"><path d="M13 21S1 13.5 1 6.5A5.5 5.5 0 0 1 13 4a5.5 5.5 0 0 1 12 2.5C25 13.5 13 21 13 21z" fill="#e8e8e8"/></svg>
  <div class="thumb hook" role="img" aria-label="Bed rail tie down hook"></div>
  <p class="name">Kodo Offroad Summit TX 900<br>Factory Bed Rail Tie Down Hook</p>
  <p class="price">$9.77</p>
</article>
<article class="card" style="left:775px;top:997px">
  <svg class="heart" width="26" height="22" viewBox="0 0 26 22"><path d="M13 21S1 13.5 1 6.5A5.5 5.5 0 0 1 13 4a5.5 5.5 0 0 1 12 2.5C25 13.5 13 21 13 21z" fill="#e8e8e8"/></svg>
  <div class="thumb flares" role="img" aria-label="Set of black fender flares"></div>
  <p class="name">Gritguard Trekker 520<br>Fender Flares</p>
  <p class="price">$169.99</p>
</article>

<section class="featured">
  <h2 class="section-title">FEATURED PRODUCTS</h2>
  <div class="arrow dim" style="left:37px;top:306px;background:#3a3a3a"><svg width="10" height="14" viewBox="0 0 10 14"><path d="M8 1L2 7l6 6" fill="none" stroke="#fff" stroke-width="2.4"/></svg></div>
  <div class="arrow dark" style="left:1126px;top:306px"><svg width="10" height="14" viewBox="0 0 10 14"><path d="M2 1l6 6-6 6" fill="none" stroke="#fff" stroke-width="2.4"/></svg></div>

  <article class="card" style="left:112px;top:144px">
    <svg class="heart" width="26" height="22" viewBox="0 0 26 22"><path d="M13 21S1 13.5 1 6.5A5.5 5.5 0 0 1 13 4a5.5 5.5 0 0 1 12 2.5C25 13.5 13 21 13 21z" fill="#e8e8e8"/></svg>
    <div class="thumb nut" role="img" aria-label="Aluminium bed rail nut"></div>
    <div class="btn qv">QUICK VIEW</div>
    <svg class="cursor" style="left:222px;top:200px" width="20" height="27" viewBox="0 0 22 30"><path d="M7 2v14l-3-3c-1.5-1.5-3.5 0-2 2l6 8c1 1.5 2 3 5 3h3c3 0 5-2 5-5v-7c0-1.5-2-1.5-2 0v-2c0-1.5-2-1.5-2 0v-1c0-1.5-2-1.5-2 0V2c0-2-3-2-3 0z" fill="#fff" stroke="#111" stroke-width="1.3"/></svg>
    <p class="name">Kodo Offroad Summit TX 900<br>Bed Rail Nut</p>
    <p class="price">$5.90</p>
  </article>
  <article class="card" style="left:443px;top:144px">
    <svg class="heart" width="26" height="22" viewBox="0 0 26 22"><path d="M13 21S1 13.5 1 6.5A5.5 5.5 0 0 1 13 4a5.5 5.5 0 0 1 12 2.5C25 13.5 13 21 13 21z" fill="#e8e8e8"/></svg>
    <div class="thumb hook" role="img" aria-label="Bed rail tie down hook"></div>
    <p class="name">Kodo Offroad Summit TX 900<br>Factory Bed Rail Tie Down Hook</p>
    <p class="price">$9.77</p>
  </article>
  <article class="card" style="left:775px;top:144px">
    <svg class="heart" width="26" height="22" viewBox="0 0 26 22"><path d="M13 21S1 13.5 1 6.5A5.5 5.5 0 0 1 13 4a5.5 5.5 0 0 1 12 2.5C25 13.5 13 21 13 21z" fill="#e8e8e8"/></svg>
    <div class="thumb flares" role="img" aria-label="Set of black fender flares"></div>
    <p class="name">Gritguard Trekker 520<br>Fender Flares</p>
    <p class="price">$169.99</p>
  </article>
</section>

<h2 class="section-title" style="top:2110px">CATEGORIES</h2>

<div class="texture" style="left:0;top:2560px;width:348px;height:546px"></div>

<article class="cat" style="left:112px;top:2218px">
  <div class="photo" role="img" aria-label="UTV rear axle assembly" style="background:radial-gradient(ellipse at 50% 50%,#4a4d52 0%,#8a8d92 40%,#ffffff 75%)"></div>
  <p class="label">Axles</p><div class="btn">QUICK VIEW</div>
</article>
<article class="cat" style="left:443px;top:2218px">
  <div class="photo" role="img" aria-label="Clutch kit with pressure plate and disc" style="background:radial-gradient(circle at 50% 45%,#7d8590 0%,#3b4650 35%,#ffffff 68%)"></div>
  <p class="label">Clutch Kits</p><div class="btn">QUICK VIEW</div>
</article>
<article class="cat" style="left:775px;top:2218px">
  <div class="photo" role="img" aria-label="UTV under a black cover outdoors" style="background:linear-gradient(180deg,#4a5a6a 0%,#2a2e33 45%,#3e5a34 100%)"></div>
  <p class="label">Car Covers</p><div class="btn">QUICK VIEW</div>
</article>
<article class="cat" style="left:112px;top:2596px">
  <div class="photo" role="img" aria-label="Assorted UTV accessories and parts" style="background:linear-gradient(180deg,#5a5a5a 0%,#2c2c2c 60%,#444 100%)"></div>
  <p class="label">Accessories</p><div class="btn">QUICK VIEW</div>
</article>
<article class="cat" style="left:443px;top:2596px">
  <div class="photo" role="img" aria-label="UTV with LED lights at night" style="background:radial-gradient(ellipse at 50% 30%,#d8c94a 0%,#3a3a20 35%,#101418 70%,#1e3a4a 100%)"></div>
  <p class="label">Lighting</p><div class="btn">QUICK VIEW</div>
</article>
<article class="cat" style="left:775px;top:2596px">
  <div class="photo" role="img" aria-label="UTV with red underglow lighting" style="background:radial-gradient(ellipse at 35% 45%,#ff2a6a 0%,#6a1a40 35%,#2a2a30 70%)"></div>
  <p class="label">Performance</p><div class="btn">QUICK VIEW</div>
</article>

<div class="learn">LEARN MORE</div>

<section class="signup" role="img" aria-label="UTV kicking up sand in the dunes">
  <div class="signup-photo"></div>
  <h2>SIGN UP AND SAVE!</h2>
  <p>Exclusive email offers &amp; Limited time</p>
  <div class="email">Enter Email ID</div>
  <div class="btn">SEARCH</div>
</section>

<footer class="footer">
  <div class="brand">TRAILRIDGE DEPOT</div>
  <div class="social"><span></span><span></span><span></span><span></span><span></span></div>
  <div class="fcol" style="left:431px">
    <h4>CATEGORIES</h4>
    <ul><li>Body &amp; Exterior</li><li>Interior &amp; Comfort</li><li>Wheels &amp; Tires</li><li>Engine Performance</li><li>Suspension &amp; Lift Kits</li><li>Drivetrain &amp; Steering</li><li>Enhancements &amp; Add-Ons</li><li>Misc.</li></ul>
  </div>
  <div class="fcol" style="left:645px">
    <h4>POLICIES</h4>
    <ul><li>Privacy Policy</li><li>Refund Policy</li><li>Terms of Service</li><li>Return Policy</li></ul>
  </div>
  <div class="fcol contact" style="left:850px">
    <h4>CONTACT</h4>
    <ul>
      <li><svg width="11" height="15" viewBox="0 0 11 15" style="margin-top:5px"><path d="M5.5 0A5.5 5.5 0 0 0 0 5.5C0 9.5 5.5 15 5.5 15S11 9.5 11 5.5A5.5 5.5 0 0 0 5.5 0z" fill="#eee"/><circle cx="5.5" cy="5.5" r="2" fill="#2d2d2d"/></svg><span>1180 Cedar Ridge Rd,<br>Branson Missouri 65616, US</span></li>
      <li><svg width="13" height="13" viewBox="0 0 13 13" style="margin-top:6px"><path d="M2.5 0l2.5 3-1.5 2c1 2 2.5 3.5 4.5 4.5l2-1.5 3 2.5-1.5 2.5C6 13 0 7 0 1.5z" fill="#eee"/></svg><span>Tel: + 4175550193</span></li>
      <li><svg width="14" height="11" viewBox="0 0 14 11" style="margin-top:7px"><rect width="14" height="11" rx="1" fill="#eee"/><path d="M0.5 1l6.5 5 6.5-5" fill="none" stroke="#2d2d2d" stroke-width="1.3"/></svg><span>info@trailridgedepot.com</span></li>
    </ul>
  </div>
  <p class="copy">2024 Trailridge Depot.<br>All Rights Reserved.</p>
</footer>

</body>
</html>
```